Call to action redesign for ~1/3 of a website i.e. the hero image

We are redesigning just the top 1/3 of brelloway.net. We need to add in a box that solves the problems that are outlined in the attached pdf.

We're looking for extremely clean and easy to understand design options.

If we like your designs there is definitely potential for picking up steady work.

Target Market(s)

Businesses

Industry/Entity Type

Call

```html
<!DOCTYPE html>
<html lang="en">
<head>
<meta charset="utf-8">
<title>Brelloway – Hero</title>
<link rel="stylesheet" href="https://fonts.googleapis.com/css2?family=Open+Sans:wght@400;600;700&family=Tinos&family=Shadows+Into+Light+Two&family=Arimo&display=swap">
<style>
  :root {
    --brand: #1a4aa6;
    --brand-dark: #0f3d8f;
    --band-top: #2a9ee0;
    --band-bottom: #0a6fc0;
    --hero-bg: #dbeaf2;
    --stat-top: #74c6ef;
    --stat-bottom: #49aee6;
    --stat-line: #a9dcf6;
    --white: #ffffff;
    --muted: #e6f4fc;
  }
  * { box-sizing: border-box; margin: 0; padding: 0; }
  html, body { width: 1200px; height: 620px; overflow: hidden; background: var(--white); }
  body { position: relative; font-family: "Open Sans", Tahoma, sans-serif; }

  .header { position: absolute; top: 0; left: 0; width: 1200px; height: 96px; }
  .brand-name { position: absolute; left: 112px; top: 22px; font-weight: 700; font-size: 40px; letter-spacing: 3px; color: var(--brand); }
  .phone { position: absolute; left: 784px; top: 38px; display: flex; align-items: center; gap: 18px; color: var(--brand); font-size: 20px; }

  .quick-links { position: absolute; top: 96px; left: 0; width: 1200px; height: 43px;
    background: linear-gradient(var(--band-top), var(--band-bottom)); border-top: 2px solid #7cc6ef;
    font-family: "Tinos", Georgia, serif; font-size: 19px; color: var(--white); }
  .quick-links .lead { position: absolute; left: 112px; top: 9px; color: #cfe9fa; }
  .quick-links .link { position: absolute; top: 9px; display: flex; align-items: center; gap: 12px; }
  .bullet { width: 20px; height: 20px; }

  .hero { position: absolute; top: 139px; left: 0; width: 1200px; height: 320px; background: var(--hero-bg); }
  .headline { position: absolute; left: 110px; top: 32px; font-family: "Shadows Into Light Two", cursive; font-size: 44px; color: var(--brand); letter-spacing: 1px; }
  .swoosh { position: absolute; left: 530px; top: 86px; }
  .intro { position: absolute; left: 110px; top: 125px; width: 540px; font-family: "Arimo", Arial, sans-serif; font-size: 13px; line-height: 17px; color: var(--brand); }
  .domain-label { position: absolute; left: 110px; top: 204px; font-family: "Shadows Into Light Two", cursive; font-size: 22px; color: var(--brand); letter-spacing: 1px; }
  .domain-input { position: absolute; left: 111px; top: 235px; width: 474px; height: 50px; background: var(--white); border: 1px solid #c9dce6; }
  .submit { position: absolute; left: 592px; top: 235px; width: 161px; height: 50px;
    background: linear-gradient(#2f97dd, #0a64b8); border: 1px solid #0a56a0; color: var(--white);
    font-size: 16px; line-height: 20px; text-align: center; padding-top: 4px; }
  .example { position: absolute; left: 110px; top: 290px; font-family: "Arimo", Arial, sans-serif; font-size: 12.5px; letter-spacing: 1px; color: var(--brand); }

  .stats { position: absolute; left: 783px; top: 0; width: 306px; height: 320px; }
  .stat { height: 79px; padding-left: 43px; color: var(--white); border-bottom: 1px solid var(--stat-line);
    background: linear-gradient(var(--stat-top), var(--stat-bottom)); }
  .stat:last-child { border-bottom: 0; height: 81px; }
  .stat-intro { font-size: 18px; line-height: 24px; padding-top: 17px; }
  .stat-value { font-size: 33px; font-weight: 600; line-height: 40px; }
  .stat-unit { font-size: 16px; color: var(--muted); font-weight: 400; }
  .stat-row { padding-top: 18px; }
  .stat-stack { padding-top: 10px; }
  .stat-stack .stat-unit { display: block; line-height: 18px; }

  .main-nav { position: absolute; top: 459px; left: 0; width: 1200px; height: 84px;
    background: linear-gradient(#1896e0, #056cbf); border-top: 2px solid #4fb2ea;
    box-shadow: 0 4px 8px rgba(0, 60, 110, 0.35); display: flex; }
  .main-nav a { color: var(--white); text-decoration: none; font-size: 19px; line-height: 80px; text-align: center; border-right: 1px solid rgba(255,255,255,0.28); }
  .main-nav a:last-child { border-right: 0; }
  .footer-fade { position: absolute; top: 543px; left: 0; width: 1200px; height: 77px; background: linear-gradient(#e3eef4, var(--white)); }
</style>
</head>
<body>
  <header class="header">
    <div class="brand-name">BRELLOWAY</div>
    <div class="phone">
      <svg width="34" height="24" viewBox="0 0 34 24" aria-hidden="true">
        <path d="M2 8 C2 2 32 2 32 8 L32 11 L24 11 L24 7 L10 7 L10 11 L2 11 Z" fill="#1a4aa6"/>
        <path d="M8 12 L26 12 L31 23 L3 23 Z" fill="#1a4aa6"/>
        <circle cx="17" cy="17" r="3.5" fill="#fff"/>
      </svg>
      <span>Call Us 303-555-0147</span>
    </div>
  </header>

  <nav class="quick-links">
    <span class="lead">Where to start?</span>
    <span class="link" style="left:280px"><svg class="bullet" viewBox="0 0 20 20"><circle cx="10" cy="10" r="10" fill="#cdeefe"/><path d="M8 5.5 L14 10 L8 14.5 Z" fill="#2a9ee0"/></svg>See our proven results</span>
    <span class="link" style="left:531px"><svg class="bullet" viewBox="0 0 20 20"><circle cx="10" cy="10" r="10" fill="#cdeefe"/><path d="M8 5.5 L14 10 L8 14.5 Z" fill="#2a9ee0"/></svg>Request a free proposal</span>
    <span class="link" style="left:783px"><svg class="bullet" viewBox="0 0 20 20"><circle cx="10" cy="10" r="10" fill="#cdeefe"/><path d="M8 5.5 L14 10 L8 14.5 Z" fill="#2a9ee0"/></svg>Search engine rankings</span>
  </nav>

  <section class="hero">
    <h1 class="headline">lorem ipsum dolor sit amet</h1>
    <svg class="swoosh" width="142" height="18" viewBox="0 0 142 18" aria-hidden="true">
      <path d="M1 8 C40 5 100 3 140 5" stroke="#1a4aa6" stroke-width="1.6" fill="none"/>
      <path d="M55 16 C80 10 110 9 138 7" stroke="#1a4aa6" stroke-width="1" fill="none"/>
    </svg>
    <p class="intro">Lorem ipsum dolor sit amet, consectetur adipisicing elit, sed do eiusmod tempor incididunt ut labore et dolore magna aliqua.</p>
    <div class="domain-label">Enter Domain Name Below</div>
    <div class="domain-input"></div>
    <div class="submit">Submit &amp;<br>Get Rankings</div>
    <div class="example">ex: http://www.yoursitename.com</div>

    <aside class="stats">
      <div class="stat stat-intro">In the last 30 days we’ve<br>helped generate</div>
      <div class="stat stat-row"><span class="stat-value">2,296,528</span> <span class="stat-unit">Leads</span></div>
      <div class="stat stat-stack"><span class="stat-value">$49,161,198</span><span class="stat-unit">in E-Commerce Sales</span></div>
      <div class="stat stat-stack"><span class="stat-value">46,206,145</span><span class="stat-unit">Search Visits</span></div>
    </aside>
  </section>

  <nav class="main-nav">
    <a href="#" style="width:207px">Home</a>
    <a href="#" style="width:199px">How it works</a>
    <a href="#" style="width:161px">Services</a>
    <a href="#" style="width:239px">SEO Case Studies</a>
    <a href="#" style="width:132px">Help</a>
    <a href="#" style="width:182px">Contact Us</a>
  </nav>
  <div class="footer-fade"></div>
</body>
</html>
```